Music portal needs a sleek mobile app design

We need an innovative, cutting edge design for our mobile app for www.loftaroundsound.com . LOFTAROUND Music is a platform that lets independent musicians upload and share their music for free. Music lovers can discover new music too.

If you visit the website, you'll get an idea of our brand colors and theme. im attaching the logo and our new discover page layout. We use "din Next LT pro" as our brand font.

We are looking for an app optimized for iOS, but can be used on Android and windows too.

Im looking for a design that flows and navigates with user intuition and is sleek, flat style in nature and has Similar apps are tunewharf, riffpantry and beatorchard.

Here are some ideas we like, but please dont copy. Come up with something similar in 'feel'

https://www.portfoliarc.net/gallery/B-TUNE-IT-Music-application/4412983

https://sketchvault.com/shots/2290518-Music-App

The most important pages/ screens for us are:
- The discover screen
- The login and sign up screens
- The splash screen
- The track player screen
- The use profile page screen
Updates

It seems no design has come close to what I was looking for so I will be requesting a refund and withdrawing this project. Thanks for your effort

Target Market(s)

music, music app, tunewharf, loftaround music, music app design

Colors
f78f20
ffcf3e
ffffff
000000

Requirements
Must have
• a sleek easy to use navigation- please create an account on loftaroundsound.com to see how the site works.
Nice to have
• Sleek screen to screen transitions
Should not have
• no 3d designs. Flat design only

```html
<!DOCTYPE html>
<html lang="en">
<head>
<meta charset="utf-8">
<title>LOFTAROUND Music – Discover</title>
<link rel="stylesheet" href="https://fonts.googleapis.com/css2?family=Barlow:wght@400;500;600&display=swap">
<style>
  :root {
    --orange: #f78f20;
    --gold: #ffcf3e;
    --white: #ffffff;
    --black: #000000;
    --ink: #1c1c1c;
    --muted: #8a8a8a;
    --canvas: #ececec;
  }
  * { box-sizing: border-box; margin: 0; padding: 0; }
  html, body { width: 800px; height: 1200px; overflow: hidden; }
  body {
    background: var(--canvas);
    font-family: "Barlow", "Helvetica Neue", Arial, sans-serif;
    color: var(--ink);
  }
  .app-screen {
    position: absolute; left: 80px; top: 40px;
    width: 640px; height: 1120px;
    background: var(--white);
    border: 8px solid var(--orange);
    display: flex; flex-direction: column;
    overflow: hidden;
  }
  .top-bar {
    height: 50px; background: var(--orange);
    display: flex; align-items: center; justify-content: space-between;
    padding: 0 18px;
  }
  .brand { display: flex; align-items: center; gap: 8px; }
  .brand-mark { width: 16px; height: 16px; background: var(--gold); }
  .brand-name { font-size: 20px; font-weight: 600; color: var(--white); letter-spacing: 0.5px; }
  .top-link { font-size: 18px; font-weight: 500; color: var(--white); }

  .section-header {
    height: 88px; display: flex; align-items: center; gap: 16px;
    padding: 0 28px;
  }
  .section-header h1 { font-size: 36px; font-weight: 500; color: var(--ink); }

  .release-grid {
    display: grid; grid-template-columns: 220px 220px;
    column-gap: 64px; row-gap: 18px;
    justify-content: center; padding-top: 4px;
  }
  .release { display: flex; flex-direction: column; }
  .cover {
    width: 220px; height: 210px; border-radius: 10px;
    position: relative;
    display: flex; align-items: center; justify-content: center;
  }
  .cover-mirage { background: linear-gradient(160deg, #c9b48e, #6f6455); }
  .cover-slowburn { background: linear-gradient(135deg, #d6dbe8, #4b5e94 55%, #b8433a); }
  .cover-static { background: linear-gradient(180deg, #9aa4ad, #dfe3e6 60%, #b9c0c6); }
  .cover-openwater { background: linear-gradient(180deg, #c9c6e6, #e9e5ef 70%, #cfc6bd); }
  .cover-lastlight { background: linear-gradient(180deg, #d7c0a2, #6a4a72 70%, #c8a98a); }
  .cover-wander { background: linear-gradient(180deg, #eeeeee, #b8bcc0); }
  .play-badge {
    width: 44px; height: 44px; border-radius: 50%;
    background: var(--gold); border: 3px solid var(--white);
    display: flex; align-items: center; justify-content: center;
  }
  .artist { font-size: 13px; color: var(--muted); margin-top: 6px; line-height: 16px; }
  .title { font-size: 27px; font-weight: 500; line-height: 30px; color: var(--ink); white-space: nowrap; }

  .player-bar {
    margin-top: auto; height: 100px; background: var(--orange);
    display: flex; align-items: center; padding: 0 18px; gap: 10px;
  }
  .transport { display: flex; gap: 8px; }
  .transport-btn {
    width: 42px; height: 42px; border-radius: 50%;
    border: 2px solid var(--white);
    display: flex; align-items: center; justify-content: center;
  }
  .now-playing { flex: 1; margin-left: 100px; }
  .now-playing-row { display: flex; justify-content: space-between; color: var(--white); font-size: 15px; }
  .progress { height: 8px; background: var(--white); margin-top: 6px; position: relative; }
  .progress-fill { position: absolute; left: 0; top: 0; bottom: 0; width: 38%; background: var(--gold); }
  .utility { display: flex; gap: 12px; margin-left: 12px; }
</style>
</head>
<body>
<main class="app-screen">
  <header class="top-bar">
    <div class="brand"><span class="brand-mark"></span><span class="brand-name">LOFTAROUND</span></div>
    <span class="top-link">Trending genres</span>
  </header>

  <div class="section-header">
    <svg width="30" height="30" viewBox="0 0 30 30" aria-hidden="true">
      <circle cx="15" cy="15" r="13" fill="none" stroke="#bbb" stroke-width="2"/>
      <path d="M17 9 L11 15 L17 21" fill="none" stroke="#bbb" stroke-width="2.5"/>
    </svg>
    <h1>New music on LOFTAROUND</h1>
  </div>

  <section class="release-grid">
    <article class="release">
      <div class="cover cover-mirage" role="img" aria-label="Album cover: figure in a warmly lit doorway">
        <span class="play-badge"><svg width="16" height="16" viewBox="0 0 16 16"><rect x="3" y="2" width="3.5" height="12" fill="#fff"/><rect x="9.5" y="2" width="3.5" height="12" fill="#fff"/></svg></span>
      </div>
      <span class="artist">Nuru Sol</span>
      <span class="title">MIRAGE</span>
    </article>
    <article class="release">
      <div class="cover cover-slowburn" role="img" aria-label="Album cover: collage with a group of musicians">
        <span class="play-badge"><svg width="16" height="16" viewBox="0 0 16 16"><path d="M4 2 L14 8 L4 14 Z" fill="#fff"/></svg></span>
      </div>
      <span class="artist">Dune Vale</span>
      <span class="title">SLOWBURN</span>
    </article>
    <article class="release">
      <div class="cover cover-static" role="img" aria-label="Album cover: a horse in a snowy landscape">
        <span class="play-badge"><svg width="16" height="16" viewBox="0 0 16 16"><path d="M4 2 L14 8 L4 14 Z" fill="#fff"/></svg></span>
      </div>
      <span class="artist">Kiva Bright</span>
      <span class="title">Static Bloom</span>
    </article>
    <article class="release">
      <div class="cover cover-openwater" role="img" aria-label="Album cover: pale sky over a beach horizon">
        <span class="play-badge"><svg width="16" height="16" viewBox="0 0 16 16"><path d="M4 2 L14 8 L4 14 Z" fill="#fff"/></svg></span>
      </div>
      <span class="artist">Hollin</span>
      <span class="title">Open Water</span>
    </article>
    <article class="release">
      <div class="cover cover-lastlight" role="img" aria-label="Album cover: portrait of a singer in a dark dress">
        <span class="play-badge"><svg width="16" height="16" viewBox="0 0 16 16"><path d="M4 2 L14 8 L4 14 Z" fill="#fff"/></svg></span>
      </div>
      <span class="artist">Iona Reed</span>
      <span class="title">Last Light</span>
    </article>
    <article class="release">
      <div class="cover cover-wander" role="img" aria-label="Album cover: band members posing together">
        <span class="play-badge"><svg width="16" height="16" viewBox="0 0 16 16"><path d="M4 2 L14 8 L4 14 Z" fill="#fff"/></svg></span>
      </div>
      <span class="artist">Birch Mallow Band</span>
      <span class="title">Wander Further</span>
    </article>
  </section>

  <footer class="player-bar">
    <div class="transport">
      <span class="transport-btn"><svg width="18" height="14" viewBox="0 0 18 14"><path d="M9 1 L2 7 L9 13 Z M16 1 L9 7 L16 13 Z" fill="#fff"/></svg></span>
      <span class="transport-btn"><svg width="14" height="14" viewBox="0 0 14 14"><rect x="2" y="1" width="3.5" height="12" fill="#fff"/><rect x="8.5" y="1" width="3.5" height="12" fill="#fff"/></svg></span>
      <span class="transport-btn"><svg width="18" height="14" viewBox="0 0 18 14"><path d="M2 1 L9 7 L2 13 Z M9 1 L16 7 L9 13 Z" fill="#fff"/></svg></span>
    </div>
    <div class="now-playing">
      <div class="now-playing-row"><span>Nuru Sol - MIRAGE</span><span>02:35</span></div>
      <div class="progress"><span class="progress-fill"></span></div>
    </div>
    <div class="utility">
      <svg width="30" height="30" viewBox="0 0 30 30" aria-label="Volume"><path d="M4 11 H9 L15 5 V25 L9 19 H4 Z" fill="none" stroke="#fff" stroke-width="2"/><path d="M19 10 Q23 15 19 20 M22 7 Q28 15 22 23" fill="none" stroke="#fff" stroke-width="2"/></svg>
      <svg width="30" height="30" viewBox="0 0 30 30" aria-label="Search"><circle cx="12" cy="12" r="8" fill="none" stroke="#fff" stroke-width="2.5"/><path d="M18 18 L27 27" stroke="#fff" stroke-width="3"/></svg>
      <svg width="30" height="30" viewBox="0 0 30 30" aria-label="Home"><path d="M3 15 L15 4 L27 15 M7 12 V26 H13 V19 H17 V26 H23 V12" fill="none" stroke="#fff" stroke-width="2.5" stroke-linejoin="round"/></svg>
    </div>
  </footer>
</main>
</body>
</html>
```